Business Card Design Project

Want a modern business card.
Concern is that our email address is long and thus poses a design challenge.
Items like the company name can be omitted from text as it will be available via the logo.

Example:
Desmond Farraway
President / CEO
Cell 555.304.2817
Office 555.619.0352
desmondf@qtvnetworkplatforms.example
www.qtvnetworkplatforms.example

Target Market(s)

Technical and executive level members of Information Technology companies in the Healthcare industry.

Industry/Entity Type

Business

Colors

Designer to choose colors to be used in the design.

Requirements
Nice to have
• Raised logo, but I am open.

```html
<!DOCTYPE html>
<html lang="en">
<head>
<meta charset="utf-8">
<title>QTV Network Platforms – Business Card</title>
<link rel="stylesheet" href="https://fonts.googleapis.com/css2?family=Open+Sans:wght@400;600;700&display=swap">
<style>
  :root {
    --stage: #e9e6e1;
    --card: #ffffff;
    --brand-blue: #25468f;
    --brand-red: #d7262c;
    --ink: #1d1d1f;
    --muted: #6b6b6b;
  }
  * { box-sizing: border-box; margin: 0; padding: 0; }
  html, body {
    width: 1200px; height: 913px; overflow: hidden;
    background: var(--stage);
    font-family: "Open Sans", Arial, sans-serif;
  }
  .stage {
    width: 1200px; height: 913px;
    display: flex; align-items: center; justify-content: center; gap: 40px;
  }
  .card {
    position: relative;
    width: 540px; height: 309px;
    background: var(--card);
    box-shadow: 0 6px 18px rgba(0,0,0,.18);
    overflow: hidden;
  }
  .wordmark {
    font-weight: 700;
    color: var(--brand-blue);
    letter-spacing: 1px;
    text-transform: uppercase;
    white-space: nowrap;
  }
  .card-front .wordmark {
    position: absolute; left: 0; right: 0; top: 132px;
    text-align: center; font-size: 34px;
  }
  .card-back .wordmark {
    position: absolute; left: 150px; top: 46px;
    font-size: 24px;
  }
  .identity {
    position: absolute; right: 40px; top: 108px; text-align: right;
  }
  .identity-name {
    font-weight: 700; font-size: 15px; color: var(--brand-blue);
  }
  .identity-title {
    font-size: 10px; color: var(--muted); margin-top: 2px;
  }
  .contact {
    position: absolute; left: 40px; bottom: 44px;
    list-style: none;
    font-size: 13px; color: var(--ink); line-height: 21px;
  }
  .contact li { display: flex; align-items: center; gap: 10px; }
  .contact svg { width: 12px; height: 12px; fill: var(--ink); flex: none; }
  .contact-text { white-space: nowrap; }
  .contact .web .contact-text { font-weight: 600; }
  .url-domain { color: var(--brand-red); }
  .band {
    position: absolute; left: 0; right: 0; bottom: 12px; height: 16px;
    display: flex;
  }
  .band-red { flex: 0 0 72%; background: var(--brand-red); }
  .band-blue { flex: 1; background: var(--brand-blue); }
</style>
</head>
<body>
<main class="stage">
  <section class="card card-front" aria-label="Card front">
    <div class="wordmark">QTV Network Platforms</div>
  </section>

  <section class="card card-back" aria-label="Card back">
    <div class="wordmark">QTV Network Platforms</div>
    <div class="identity">
      <div class="identity-name">Desmond Farraway</div>
      <div class="identity-title">President / CEO</div>
    </div>
    <ul class="contact">
      <li>
        <svg viewBox="0 0 12 12" aria-hidden="true"><rect x="3" y="0" width="6" height="12" rx="1"/><rect x="4" y="1.5" width="4" height="7" fill="#fff"/></svg>
        <span class="contact-text">555.304.2817</span>
      </li>
      <li>
        <svg viewBox="0 0 12 12" aria-hidden="true"><path d="M1 4c0-2 2-3 5-3s5 1 5 3l-3 0 0-1H4v1zM2 6h8l1 5H1z"/></svg>
        <span class="contact-text">555.619.0352</span>
      </li>
      <li>
        <svg viewBox="0 0 12 12" aria-hidden="true"><rect x="0" y="2" width="12" height="8"/><path d="M0.5 2.5 6 7l5.5-4.5" stroke="#fff" fill="none"/></svg>
        <span class="contact-text">desmondf@qtvnetworkplatforms.example</span>
      </li>
      <li class="web">
        <svg viewBox="0 0 12 12" aria-hidden="true"><circle cx="6" cy="6" r="6"/><path d="M0 6h12M6 0v12M6 0c-3 3-3 9 0 12M6 0c3 3 3 9 0 12" stroke="#fff" stroke-width=".8" fill="none"/></svg>
        <span class="contact-text">www.<span class="url-domain">qtvnetworkplatforms</span>.example</span>
      </li>
    </ul>
    <div class="band"><div class="band-red"></div><div class="band-blue"></div></div>
  </section>
</main>
</body>
</html>
```